Design a Brochure for my company to describe our services

-VERY IMPORTANT, THE REAL ATTACHED FILE IS "BLUMWEIDEN BROCHURE TELVA". YOU CAN DELETE "BROCHURE", IT'S THE WRONG FILE.

Hi Freelancers,

I need a Brochure design,6 Pages (105mm/210mm Hoch) to describe the services / Products we provide.

Every texts and images are in a Word document attached.

The main point of this brochure is to invite everybody to visit our company and to see what product we sell and what services we offer.

The main color should be Black / Orange.

I want you to create a nice design, nice font. The brochure needs to catch everybody's attention.

Please be very creative with the design, you can get inspiration from our website also [url removed, login to view]

Thanks and good luck with the design

```html
<!DOCTYPE html>
<html lang="fr">
<head>
<meta charset="utf-8">
<title>Blumweiden – Brochure intérieur</title>
<link href="https://fonts.googleapis.com/css2?family=Arimo:wght@400;700&family=Varela+Round&display=swap" rel="stylesheet">
<style>
  :root{
    --black:#1b1716;
    --orange:#e8661f;
    --white:#ffffff;
    --ink:#1d1d1d;
    --photo-kitchen:#b9b3ad;
    --photo-kitchen-dark:#6e6660;
    --photo-stove:#e9e6e2;
    --photo-fire:#3b2a22;
    --photo-bath:#5c5a5c;
    --photo-bath-light:#9a9899;
  }
  *{margin:0;padding:0;box-sizing:border-box}
  html,body{width:1200px;height:848px;overflow:hidden;background:var(--white)}
  .spread{position:relative;width:1200px;height:848px;display:flex}
  .panel{position:relative;width:400px;height:848px;overflow:hidden}
  .panel--kitchen{background:var(--black)}
  .panel--stoves{background:var(--orange)}
  .panel--bath{background:var(--black)}
  .abs{position:absolute}
  .photo{position:absolute;display:block}

  h2{font-family:"Arimo",Arial,sans-serif;font-weight:700;font-size:21px;line-height:24px;letter-spacing:.2px}
  h3{font-family:"Arimo",Arial,sans-serif;font-weight:700;font-size:15.5px;line-height:20px}
  .round{font-family:"Varela Round","Arimo",sans-serif}

  /* Cuisines */
  .kitchen-title{left:32px;top:40px;color:var(--orange)}
  .kitchen-intro{left:32px;top:72px;width:345px;font-family:"Arimo",Arial,sans-serif;font-size:15.5px;line-height:25px;color:var(--white);text-align:justify}
  .kitchen-band{left:0;top:600px;width:400px;height:248px;background:var(--white)}
  .kitchen-body{left:33px;top:633px;width:340px;font-family:"Arimo",Arial,sans-serif;font-size:13.4px;line-height:25.5px;color:var(--ink);text-align:justify}

  /* Poêles */
  .stoves-title{left:433px;top:40px;color:var(--white)}
  .stoves-intro{left:433px;top:70px;width:338px;font-size:12.2px;line-height:20.5px;color:var(--ink);text-align:justify}
  .stoves-photo{left:433px;top:149px;width:338px;height:333px;border-radius:14px;background:linear-gradient(160deg,#f4f2ef,var(--photo-stove) 60%,#cfc9c3)}
  .fire-photo{left:624px;top:456px;width:136px;height:134px;border-radius:12px;border:3px solid var(--white);background:radial-gradient(circle at 45% 45%,#e07a28,var(--photo-fire) 60%,#d9d5d0 62%)}
  .stoves-brands{left:433px;top:494px;width:182px;font-size:12.4px;line-height:19.5px;color:var(--ink);letter-spacing:.4px;text-align:justify}
  .appliance-title{left:433px;top:612px;color:var(--white)}
  .appliance-body{left:433px;top:640px;width:340px;font-size:12.2px;line-height:18px;color:var(--ink)}
  .appliance-list-title{left:433px;top:698px;font-size:12.2px;line-height:18px;font-weight:700;color:var(--white);font-family:"Arimo",Arial,sans-serif}
  .appliance-list{left:433px;top:718px;width:280px;display:grid;grid-template-columns:140px 140px;list-style:none;font-size:12.2px;line-height:19.5px;color:var(--ink)}
  .appliance-list li::before{content:"• "}
  .appliance-brands{left:433px;top:788px;width:345px;font-size:12.2px;line-height:18px;color:var(--ink)}

  /* Salle de bains */
  .bath-title{left:827px;top:40px;color:var(--orange)}
  .bath-intro{left:827px;top:70px;width:198px;font-size:13.4px;line-height:19.5px;color:var(--white)}
  .basin-photo{left:1033px;top:0;width:152px;height:197px;border:3px solid var(--orange);border-top:none;border-radius:0 0 6px 6px;background:radial-gradient(circle at 50% 55%,#2f2e30 0 18%,#8b898a 30%,var(--photo-bath-light) 60%,#c7c5c4)}
  .bath-photo{left:827px;top:217px;width:353px;height:205px;border-radius:4px;background:linear-gradient(180deg,var(--photo-bath) 0%,#7a7879 55%,#b9b7b5 100%)}
  .dressing-title{left:827px;top:437px;color:var(--orange)}
  .dressing-body{left:827px;top:472px;width:348px;font-size:12.2px;line-height:20px;color:var(--white);text-align:justify}
  .dressing-body p+p{margin-top:7px}
  .divider{left:827px;top:710px;width:346px;height:2px;background:var(--white)}
  .expo-title{left:827px;top:726px;color:var(--orange);font-size:16.5px}
  .expo-body{left:827px;top:756px;width:350px;font-size:12.6px;line-height:19.5px;color:var(--white);text-align:justify;text-indent:42px}
  .expo-body b{font-family:"Arimo",Arial,sans-serif;font-weight:700}
</style>
</head>
<body>
<main class="spread">

  <section class="panel panel--kitchen">
    <svg class="abs" width="400" height="848" viewBox="0 0 400 848" aria-hidden="true">
      <polygon points="0,390 185,362 200,376 215,362 400,390 400,600 0,600" fill="var(--orange)"/>
      <polygon points="185,362 200,376 215,362" fill="var(--white)"/>
    </svg>
    <div class="kitchen-band abs"></div>

    <h2 class="abs kitchen-title">Cuisines</h2>
    <p class="abs kitchen-intro">La cuisine est l'un des endroits du foyer où la créativité n'a pas de limites. Venez découvriez nos cuisines exposées. De plus, nous proposons également les fours à pains et fours à pizzas.</p>

    <div class="photo" role="img" aria-label="Détail d'une cuisine moderne avec robinet chromé" style="left:29px;top:203px;width:118px;height:157px;border:2px solid var(--white);border-radius:4px;background:linear-gradient(160deg,#f1efec,#c9c4c0 60%,#7a6060)"></div>
    <div class="photo" role="img" aria-label="Cuisine exposée avec îlot blanc et suspensions orange" style="left:164px;top:203px;width:209px;height:157px;border:2px solid var(--white);border-radius:4px;background:linear-gradient(170deg,#d8d2cc,var(--photo-kitchen) 50%,#8a6c52)"></div>
    <div class="photo" role="img" aria-label="Grande cuisine ouverte avec îlot et façades violettes" style="left:29px;top:376px;width:344px;height:227px;border:2px solid var(--white);border-radius:6px;background:linear-gradient(180deg,#e4e1de,var(--photo-kitchen) 55%,var(--photo-kitchen-dark))"></div>

    <p class="abs kitchen-body">Un logiciel de dessin permet aux clients de visionner leurs projets en 3D. La créativité n'a de sens qui si on peut la visualiser en se projetant dans son futur intérieur. C'est l'une des grandes forces de cet outil informatique, et bien évidemment de notre showroom. Nous travaillons avec plusieurs marques reconnues telles que Modalis, etc.</p>
  </section>

  <section class="panel panel--stoves"></section>
  <section class="panel panel--bath"></section>

  <h2 class="abs stoves-title">Poêles et cheminées</h2>
  <p class="abs round stoves-intro">Nous sommes spécialisés dans la pose de poêles et cheminées. Aucun soucis, nous nous occupons aussi du tubage. Nous avons dans notre assortiment des poêles standard ainsi que des poêles de masse.</p>
  <div class="photo stoves-photo" role="img" aria-label="Poêle à bois noir allumé dans un intérieur clair"></div>
  <div class="photo fire-photo" role="img" aria-label="Foyer ouvert avec braises"></div>
  <p class="abs round stoves-brands">Nous travaillons avec plusieurs marques reconnues telles que Haldor, Kivalo, Harvendal, OSTRA, Frelan Cheminée, etc.</p>

  <h3 class="abs appliance-title">Electroménager</h3>
  <p class="abs round appliance-body">Vous trouverez dans notre assortiment un grand choix d'appareil électroménager pour tout budget. Optez pour le meilleur rapport qualité / prix !</p>
  <p class="abs appliance-list-title">Nous avons en exposition :</p>
  <ul class="abs round appliance-list">
    <li>Machines à laver</li><li>Réfrigérateurs</li>
    <li>Sèches linge</li><li>Etc.</li>
    <li>Cave à vins</li>
  </ul>
  <p class="abs round appliance-brands">Nous travaillons avec plusieurs marques reconnues telles que Arvel-Lumex, Morav, Bertan, Sorvik, etc.</p>

  <h2 class="abs bath-title">Salle de bains</h2>
  <p class="abs round bath-intro">Aménager une salle d'eau n'est pas toujours aisée. Notre compétence et notre expérience nous permettent d'aménager des espaces design dans votre salle de bains.</p>
  <div class="photo basin-photo" role="img" aria-label="Vasque en pierre ronde"></div>
  <div class="photo bath-photo" role="img" aria-label="Salle de bains design aux tons gris avec double vasque"></div>

  <h2 class="abs dressing-title">Dressing &amp; rangements</h2>
  <div class="abs round dressing-body">
    <p>Le dressing en anglais ou garde-robe est un espace aménagé spécifiquement pour les habits.</p>
    <p>Le dressing doit être choisi en fonction de son usage au quotidien et de la place qu'on souhaite lui accordée. L'avantage du dressing est l'organisation des vêtements et la facilité à l'accessibilité.</p>
    <p>Selon votre budget et vos envies, nous proposons de nombreux dressing répondant à vos attentes. De plus, nous avons un vaste choix de meubles de rangements de qualité.</p>
  </div>
  <div class="abs divider"></div>
  <h3 class="abs expo-title">Notre exposition</h3>
  <p class="abs round expo-body">Plus de <b>1000 m2</b> d'exposition sur 3 étages sont aménagés dans notre showroom à Telva. De plus, chaque jeudi soir le magasin ouvre jusqu'à 20h00.</p>

</main>
</body>
</html>
```